Design a Marketing Brochure for IT Security Solution

Verondel Security provides network security for small and medium businesses. We sell through the IT channel -- which means our product is sold and serviced by IT service companies across the US. We consider these companies our "partners" or "reseller partners." They buy our product and service, then deliver it to their clients. Our one and only product is the PortWarden UTM firewall.

As part of the latest release of PortWarden, we’ve introduced the Hallmonitor feature. We want to provide our partners with a marketing brochure that they can use to educate their customers about Hallmonitor. The landing page at www.verondel-example.com/hallmonitor will give you more information about the feature.

Target Market(s)

This brochure will be made available to our partners to market the Hallmonitor product.

Colors
ec1f27

Requirements
Must have
• Create a two-page flyer in an adobe program (InDesign, Photoshop, Acrobat). The flyer should be created for high-quality print, 300 dpi, full bleed. Use the provided text (see attached word doc) and logo (see attached eps file). The style of the flyer should be similar to our display banner (see attached image of banner mock-up). Deliverables should include a print-quality PDF and all adobe design files.
Verondel logo
Hallmonitor logo
Space for our reseller partners to put their own logo and contact info

```html
<!DOCTYPE html>
<html lang="en">
<head>
<meta charset="utf-8">
<title>Understanding Hallmonitor – Partner Flyer</title>
<link href="https://fonts.googleapis.com/css2?family=Open+Sans:wght@400;600;700&display=swap" rel="stylesheet">
<style>
  :root {
    --brand-red: #ec1f27;
    --ink-dark: #2b2b36;
    --ink-text: #2e2e35;
    --paper: #f3f2ee;
    --panel-pink: #f1c0ae;
    --icon-tint: #f2d6cf;
    --stage: #e9e6e1;
    --muted: #9a9ba0;
    --white: #ffffff;
  }
  * { box-sizing: border-box; margin: 0; padding: 0; }
  html, body { width: 1200px; height: 900px; overflow: hidden; }
  body {
    background: var(--stage);
    font-family: "Open Sans", Arial, sans-serif;
    color: var(--ink-text);
    position: relative;
  }
  .flyer {
    position: absolute; left: 290px; top: 12px;
    width: 620px; height: 876px;
    background: var(--paper);
    overflow: hidden;
    box-shadow: 0 6px 20px rgba(0,0,0,.15);
  }
  .top-band { position: absolute; left: 0; top: 0; width: 620px; height: 120px; }
  .section-title {
    position: absolute; left: 0; top: 72px; height: 40px; width: 330px;
    padding-left: 24px; line-height: 40px;
    color: var(--white); font-weight: 600; font-size: 20px;
  }
  .ssh-icon { position: absolute; right: 24px; top: 70px; }

  .body-text { font-size: 12px; line-height: 18px; }

  .intro { position: absolute; left: 24px; top: 134px; width: 560px; }
  .intro-item { position: relative; padding-left: 36px; margin-bottom: 8px; }
  .intro-item::before {
    content: ""; position: absolute; left: 0; top: 8px; width: 26px; height: 2px; background: var(--brand-red);
  }
  .intro-item::after {
    content: ""; position: absolute; left: 24px; top: 5px; width: 8px; height: 8px;
    border: 2px solid var(--brand-red); border-radius: 50%; background: var(--paper);
  }
  .offer-intro { padding-left: 36px; }

  .features { position: absolute; left: 60px; top: 292px; width: 530px; }
  .feature { display: flex; gap: 18px; margin-bottom: 10px; align-items: flex-start; }
  .feature:last-child { margin-bottom: 0; }
  .feature-icon { flex: 0 0 56px; height: 44px; border-radius: 6px; background: var(--icon-tint); margin-top: 2px; }
  .feature p { flex: 1; }

  .benefits {
    position: absolute; left: 24px; top: 500px; width: 572px; z-index: 2;
    background: var(--panel-pink); border-radius: 18px;
    padding: 18px 24px 16px 24px;
  }
  .benefit-list { list-style: none; width: 390px; }
  .benefit-list li { position: relative; padding-left: 24px; margin-bottom: 6px; }
  .benefit-list li:last-child { margin-bottom: 0; }
  .benefit-list svg { position: absolute; left: 0; top: 3px; }
  .feature-mark {
    position: absolute; right: 26px; top: 32px; width: 130px;
    display: flex; flex-direction: column; align-items: center; gap: 10px;
  }
  .feature-mark .dot { width: 70px; height: 70px; border-radius: 50%; background: var(--brand-red); }
  .feature-mark .name { font-size: 17px; font-weight: 600; color: var(--ink-dark); }

  .partner-space {
    position: absolute; left: 0; top: 700px; width: 620px; height: 100px;
    background: linear-gradient(180deg, #cfcfcf 0%, #ededed 60%, #e2e2e2 100%);
    display: flex; align-items: center; justify-content: center; padding-top: 10px;
    font-size: 24px; color: var(--muted); letter-spacing: .5px;
  }
  .footer { position: absolute; left: 0; top: 800px; width: 620px; height: 76px; background: var(--ink-dark); }
  .question-tab {
    position: absolute; left: 210px; top: -14px; height: 24px; padding: 0 24px;
    background: var(--brand-red); color: var(--white);
    font-size: 12px; font-weight: 700; line-height: 24px;
    clip-path: polygon(12px 0, 100% 0, calc(100% - 12px) 100%, 0 100%);
  }
  .contact { position: absolute; left: 28px; top: 26px; color: var(--white); font-size: 24px; font-weight: 600; }
  .website {
    position: absolute; right: 24px; top: 30px; color: var(--white); font-size: 14px;
    display: flex; align-items: center; gap: 8px;
  }
</style>
</head>
<body>
  <article class="flyer">
    <svg class="top-band" viewBox="0 0 620 120" aria-hidden="true">
      <polygon points="0,60 620,0 620,34 0,118" fill="var(--ink-dark)"/>
      <polygon points="0,72 350,72 330,112 0,112" fill="var(--brand-red)"/>
    </svg>
    <h1 class="section-title">Understanding Hallmonitor</h1>
    <svg class="ssh-icon" width="74" height="40" viewBox="0 0 74 40" aria-label="Secure Shell icon" role="img">
      <line x1="0" y1="22" x2="74" y2="22" stroke="var(--brand-red)" stroke-width="2"/>
      <rect x="12" y="6" width="50" height="28" rx="10" fill="var(--paper)" stroke="var(--brand-red)" stroke-width="2.5"/>
      <text x="37" y="25" text-anchor="middle" font-size="11" font-weight="700" fill="var(--brand-red)" font-family="Open Sans, sans-serif">SSH</text>
    </svg>

    <section class="intro body-text">
      <p class="intro-item">Hallmonitor provides authenticated remote access without having to expose the RDP or Secure Shell (SSH) port to the public Internet.</p>
      <p class="intro-item">Unlike traditional port forwarding, Hallmonitor requires end users to authenticate themselves via their AD credentials and a Two-Factor Authentication (2FA) verification code before they are allowed to access the destination host.</p>
      <p class="offer-intro">The secure and convenient Hallmonitor feature works with multiple mobile devices to offer:</p>
    </section>

    <section class="features body-text">
      <div class="feature">
        <div class="feature-icon" role="img" aria-label="Line icon of a user signing in"></div>
        <p>Multi-factor authentication (MFA) - only users that have been authenticated using their name and password as well as an account-specific Hallmonitor One-Time Verification Code can gain access to the business's RDP or SSH end point</p>
      </div>
      <div class="feature">
        <div class="feature-icon" role="img" aria-label="Line icon of users and access rules"></div>
        <p>Administrator defined rules to grant users, or sets of users, controlled access to specified internal resources</p>
      </div>
      <div class="feature">
        <div class="feature-icon" role="img" aria-label="Line icon of a secured server"></div>
        <p>Secure, one time, source-specific transient firewall rules minimizing exposure to the outside world as the Hallmonitor portal creates a specialized connection to the end user's IP address that isn't visible to bad actors scanning for RDP targets</p>
      </div>
    </section>

    <section class="benefits">
      <ul class="benefit-list body-text">
        <li><svg width="14" height="12" viewBox="0 0 14 12" aria-hidden="true"><path d="M1 6 L5 10 L13 1" fill="none" stroke="var(--brand-red)" stroke-width="2.5"/></svg>Unlike a VPN, Hallmonitor does not require a client software installation.</li>
        <li><svg width="14" height="12" viewBox="0 0 14 12" aria-hidden="true"><path d="M1 6 L5 10 L13 1" fill="none" stroke="var(--brand-red)" stroke-width="2.5"/></svg>Hallmonitor addresses compliance requirements and facilitates adoption of best practices, including many outlined by NIST 800-53 and NIST 800-171.</li>
        <li><svg width="14" height="12" viewBox="0 0 14 12" aria-hidden="true"><path d="M1 6 L5 10 L13 1" fill="none" stroke="var(--brand-red)" stroke-width="2.5"/></svg>Hallmonitor, a feature of Verondel's PortWarden v5.0 and later, can be used with all types of devices (Windows, iOS, Android &amp; more).</li>
      </ul>
      <div class="feature-mark">
        <span class="dot" aria-hidden="true"></span>
        <span class="name">Hallmonitor</span>
      </div>
    </section>

    <div class="partner-space">space for partner clients to add their own logo</div>

    <footer class="footer">
      <div class="question-tab">Questions about Hallmonitor?</div>
      <p class="contact">Contact us: 555.010.0199</p>
      <p class="website">
        <svg width="16" height="16" viewBox="0 0 16 16" aria-hidden="true" fill="none" stroke="var(--white)" stroke-width="1.2">
          <circle cx="8" cy="8" r="7"/><ellipse cx="8" cy="8" rx="3" ry="7"/><line x1="1" y1="8" x2="15" y2="8"/>
        </svg>
        www.verondel-example.com
      </p>
    </footer>
  </article>
</body>
</html>
```